A new website for Electrical Contractor Business

We are looking for a unique and new WordPress website design which would include 5 Pages - Home Page, Meet the Team, Our Services, Our Projects and Contact Us page.

The global theme for the website needs to be professional but simple to navigate as we cater for both business and home owner customers.

Our core business service is targeted around lighting from single room decorative to large office so the theme should incorporate this in some way.

The home page should include;
Our business logo, Contact number, Email address, small Image rotation box - Highlighting pervious projectsText box - With welcome message, chirpnet feed news reel/Customer feed back box.

I would also like to see a 2 boxes for the separate customer types we services. Business and Home Owner. each box will have a small image with a small text description with a link to the area of the services page relevant to that customer type.

Meet the team page -This will be introducing potential customers to the team so I would like it to include for each team member. Something like a small image and text area which will introduce an outline of the team members skills and abilities.

Our Services page This page will be outlining the different services on offer to the both customer types business and homeowner. Each service should have an image with text description of the service would good here.

Our projects page-Will include images of pervious projects and work we have completed along with a text area for the project description/ outliner.

Contact Us page - Should include a contact form which should include an option for the customer to quest us to call them back, also a selection box for them to inform us our how they found our details would be good.

Colour - The theme colours can be taken from the logo or feel free to impress with your own imagination.

Remember we are looking for a website that will interest our customers enough to except our services or be drawn further into the website.. So call to action links to other areas of the site/ contact page are welcome

Target Market(s)

Business - Office, warehousing and Large Store - lighting and Power
Home owner lighting and power

Coding

Coded - Design and coding required

Number of Pages Required

5+ page

Font styles to use
Serif
Sans Serif

Colors

Designer to choose colors to be used in the design.

Requirements
Must have
• Logo integrated into the website design - i.e. website colours which allow the logo to blend into the design.
Nice to have
• Custom but professional theme catering to business customers, but also show that we do provide services to home owners too.
Should not have
• Sorry am not interested in one oversized block image on rotation covering half the home page.. Images will be needed but not a single block over sized frame with not text, shape. Please use your imagination when considering this design

```html
<!DOCTYPE html>
<html lang="en">
<head>
<meta charset="utf-8">
<title>Voltline Systems – Electrical Contractors</title>
<link rel="stylesheet" href="https://fonts.googleapis.com/css2?family=Jost:wght@400;500;600;700&display=swap">
<style>
:root{
  --orange:#f26a2e;
  --orange-dark:#d9561d;
  --orange-soft:#f5a47c;
  --navy:#24345f;
  --navy-deep:#1b2849;
  --navy-darker:#15203c;
  --beige:#e4ded4;
  --grey-bg:#efefef;
  --text:#333;
  --muted:#777;
  --white:#fff;
}
*{box-sizing:border-box;margin:0;padding:0}
html,body{width:1200px;height:4138px;overflow:hidden}
body{font-family:'Jost',sans-serif;color:var(--text);background:var(--white);position:relative}
section,header,footer{position:absolute;left:0;width:1200px}
.ph{position:absolute}
.btn{position:absolute;display:flex;align-items:center;height:36px;padding:0 20px 0 6px;border-radius:18px;font-size:14px;font-weight:500;color:var(--white);letter-spacing:.5px;text-transform:uppercase;white-space:nowrap}
.btn::before{content:"";width:26px;height:26px;border-radius:50%;background:var(--white);margin-right:10px;box-shadow:inset 0 0 0 7px var(--orange)}
.btn-navy{background:var(--navy)}
.btn-orange{background:var(--orange)}
.btn-orange::before{box-shadow:inset 0 0 0 7px var(--navy)}
.sec-title{position:absolute;left:0;width:1200px;text-align:center;font-size:27px;font-weight:500;letter-spacing:1px;color:var(--navy);text-transform:uppercase}
.sec-title span{color:var(--orange)}

/* header */
.site-header{top:0;height:121px;background:var(--white)}
.topbar{position:absolute;right:0;top:0;width:565px;height:44px;background:var(--navy);clip-path:polygon(30px 0,100% 0,100% 100%,0 100%);display:flex;align-items:center;padding-left:90px;gap:40px;color:var(--white);font-size:15px}
.topbar .item{display:flex;align-items:center;gap:10px}
.topbar .dot{width:22px;height:22px;border-radius:50%;background:var(--white);display:flex;align-items:center;justify-content:center}
.brand{position:absolute;left:138px;top:18px;display:flex;flex-direction:column;align-items:center}
.brand .mark{width:54px;height:54px;border-radius:50%;background:var(--navy)}
.brand .name{margin-top:6px;font-size:17px;font-weight:600;color:var(--navy);letter-spacing:1px;text-transform:uppercase}
.main-nav{position:absolute;top:78px;left:530px;display:flex;gap:46px;font-size:15px;font-weight:500;text-transform:uppercase;color:var(--navy)}
.main-nav .active{color:var(--orange);border-bottom:2px solid var(--orange);padding-bottom:3px}

/* hero */
.hero{top:121px;height:367px;background:linear-gradient(90deg,var(--beige) 0%,#dcd6cb 45%,#cfcdc8 100%)}
.hero .ph{left:560px;top:0;width:640px;height:367px;background:linear-gradient(120deg,#c7c3bb 0%,#6c7a8c 50%,#2f4466 100%)}
.hero h1{position:absolute;left:146px;top:62px;font-size:52px;line-height:68px;font-weight:600;color:var(--navy-deep)}
.hero h1 span{color:var(--orange)}
.hero .sub{position:absolute;left:146px;top:210px;font-size:26px;color:var(--navy-deep)}
.hero .phone{position:absolute;left:146px;top:250px;font-size:34px;font-weight:500;color:var(--navy-deep)}

/* about */
.about{top:488px;height:541px}
.about .ring{position:absolute;left:118px;top:60px;width:346px;height:346px;border-radius:50%;background:#8d98ad}
.about .ph{left:140px;top:82px;width:302px;height:302px;border-radius:50%;background:linear-gradient(160deg,#f2f2f2,#d9dde4 60%,#b8c0cf)}
.about .accent{position:absolute;left:436px;top:200px;width:48px;height:90px;border-radius:6px;background:linear-gradient(180deg,var(--orange-soft),var(--orange))}
.about .kicker{position:absolute;left:571px;top:122px;font-size:24px;color:var(--navy);text-transform:uppercase}
.about h2{position:absolute;left:571px;top:152px;font-size:24px;font-weight:400;color:var(--orange);text-transform:uppercase}
.about p{position:absolute;left:571px;top:195px;width:490px;font-size:13.5px;line-height:21px;color:var(--muted)}
.about .btn{left:571px;top:374px}

/* services */
.services{top:1029px;height:580px;background:var(--grey-bg)}
.services .sec-title{top:80px}
.svc{position:absolute;top:146px;width:600px;height:434px;color:var(--white);text-align:center}
.svc-business{left:0;background:linear-gradient(135deg,#f47a3e,var(--orange-dark))}
.svc-home{left:600px;background:linear-gradient(135deg,#34466f,var(--navy-deep))}
.svc .frame,.svc .frame2{position:absolute;left:140px;top:66px;width:440px;height:330px}
.svc .frame{border-top:2px solid rgba(255,255,255,.7);border-left:2px solid rgba(255,255,255,.7);clip-path:polygon(0 0,15% 0,15% 40%,0 40%)}
.svc .frame2{border-right:2px solid rgba(255,255,255,.7);border-bottom:2px solid rgba(255,255,255,.7);clip-path:polygon(85% 60%,100% 60%,100% 100%,85% 100%)}
.svc-business .frame,.svc-business .frame2{left:140px}
.svc-home .frame,.svc-home .frame2{left:26px}
.svc h3{position:absolute;top:100px;width:100%;font-size:28px;font-weight:400}
.svc p{position:absolute;top:146px;left:90px;width:420px;font-size:13px;line-height:21px;opacity:.95}
.svc .btn{top:294px;left:240px}
.services .notch{position:absolute;left:570px;top:146px;width:0;height:0;border-left:30px solid transparent;border-right:30px solid transparent;border-top:30px solid var(--grey-bg)}

/* testimonials */
.testimonials{top:1609px;height:576px}
.testimonials .sec-title{top:80px}
.quote-card{position:absolute;top:146px;width:380px;height:204px;background:var(--white);padding:34px 48px;font-size:13px;line-height:21px;text-align:center}
.quote-card.side{opacity:.3;box-shadow:0 0 14px rgba(0,0,0,.06)}
.quote-card.center{left:417px;width:367px;height:210px;top:146px;padding:30px 44px;box-shadow:0 4px 20px rgba(0,0,0,.18);z-index:2}
.quote-card .q{position:absolute;font-size:60px;line-height:1;color:#bbb;font-weight:700}
.quote-card .stars{margin-top:14px;display:flex;gap:4px;justify-content:center}
.avatar{position:absolute;left:563px;top:400px;width:74px;height:74px;border-radius:50%;border:3px solid var(--navy);background:linear-gradient(#c9ced8,#8a96ad)}
.client-name{position:absolute;top:478px;width:1200px;text-align:center;font-size:17px;color:var(--orange)}

/* emergency */
.emergency{top:2185px;height:265px;background:linear-gradient(90deg,#2b2c2f,#3a3b3e 60%,#2b2c2f)}
.emergency .ph{left:207px;top:-48px;width:234px;height:313px;background:linear-gradient(180deg,#e3b336 0,#8a7a68 25%,#5d6b7e 60%,#4a3f36);border-radius:40px 40px 6px 6px}
.emergency h2{position:absolute;left:521px;top:56px;font-size:28px;font-weight:500;color:var(--white);letter-spacing:.5px}
.emergency p{position:absolute;left:521px;top:98px;width:500px;font-size:17px;line-height:25px;color:var(--white)}
.emergency .btn{left:521px;top:164px}

/* team */
.team{top:2450px;height:618px}
.team .sec-title{top:78px}
.member{position:absolute;top:144px;width:212px;height:331px;background:#eaeaea}
.member .ph{left:0;top:0;width:212px;height:331px}
.member-card{position:absolute;left:0;bottom:0;width:212px;height:152px;background:var(--orange);color:var(--white);text-align:center;clip-path:polygon(0 18%,50% 0,100% 18%,100% 100%,0 100%)}
.member-card h4{margin-top:44px;font-size:18px;font-weight:400}
.member-card .role{font-size:13px;opacity:.9}
.member-card .socials{margin-top:10px;display:flex;justify-content:center;gap:5px}
.member-card .socials i{width:18px;height:18px;background:var(--navy);display:block}
.team .btn{left:533px;top:512px}

/* projects */
.projects{top:3068px;height:712px;background:var(--grey-bg)}
.projects .sec-title{top:80px}
.tile{position:absolute}
.tile-hover{background:var(--navy);color:var(--white);text-align:center;display:flex;flex-direction:column;align-items:center;justify-content:center;font-size:15px;line-height:21px;padding:0 30px}
.tile-hover .plus{width:34px;height:34px;border-radius:50%;border:2px solid var(--white);font-size:24px;line-height:28px;margin-bottom:18px}
.projects .btn{left:533px;top:594px}

/* footer */
.site-footer{top:3780px;height:315px;background:var(--navy-deep);color:var(--white)}
.f-col{position:absolute;top:68px}
.f-col h5{font-size:13px;font-weight:500;letter-spacing:.5px;text-transform:uppercase;margin-bottom:14px}
.f-links li{list-style:none;font-size:13px;line-height:27px}
.f-links li::before{content:"›";margin-right:8px}
.f-contact .row{display:flex;gap:10px;font-size:13px;line-height:18px;margin-bottom:14px}
.f-contact .row b{font-weight:500}
.f-contact .ic{width:12px;flex:none;margin-top:3px}
.feed{display:flex;gap:10px;margin-bottom:18px}
.feed .sq{width:26px;height:26px;background:#2d9fd9;flex:none}
.feed .t{font-size:12px;line-height:15px}
.feed .t b{font-weight:500;display:block}
.view-all{position:absolute;left:775px;top:68px;font-size:13px;text-decoration:underline}
.f-brand{position:absolute;left:880px;top:88px;width:200px;text-align:center}
.f-brand .mark{width:54px;height:54px;border-radius:50%;background:var(--white);margin:0 auto}
.f-brand .name{margin-top:8px;font-size:16px;font-weight:600;letter-spacing:1px;text-transform:uppercase;white-space:nowrap}
.f-social{display:flex;justify-content:center;gap:8px;margin-top:22px}
.f-social i{width:28px;height:28px;border:1.5px solid var(--white);border-radius:50%;display:block}
.copyright{position:absolute;left:0;top:4095px;width:1200px;height:43px;background:var(--navy-darker);color:#c9cfdd;font-size:12px;display:flex;align-items:center;justify-content:center}
</style>
</head>
<body>

<header class="site-header">
  <div class="topbar">
    <div class="item"><span class="dot"><svg width="12" height="12" viewBox="0 0 24 24"><path fill="#24345f" d="M6.6 10.8a15 15 0 006.6 6.6l2.2-2.2c.3-.3.7-.4 1-.2 1.1.4 2.3.6 3.6.6.6 0 1 .4 1 1V20c0 .6-.4 1-1 1A17 17 0 013 4c0-.6.4-1 1-1h3.5c.6 0 1 .4 1 1 0 1.3.2 2.5.6 3.6.1.3 0 .7-.2 1z"/></svg></span>123.456.7890</div>
    <div class="item"><span class="dot"><svg width="12" height="12" viewBox="0 0 24 24"><path fill="#24345f" d="M2 5h20v14H2zm2 2v.5l8 5 8-5V7z"/></svg></span>info@voltlinesys.com</div>
  </div>
  <div class="brand"><div class="mark"></div><div class="name">Voltline Systems</div></div>
  <nav class="main-nav">
    <span class="active">Home</span><span>Meet the Team</span><span>Services</span><span>Projects</span><span>Contact Us</span>
  </nav>
</header>

<section class="hero">
  <div class="ph" role="img" aria-label="Electrician in a hard hat wiring a distribution board"></div>
  <h1>We Are <span>Always</span><br>Ready to Services</h1>
  <div class="sub">For Immediate Services Dial</div>
  <div class="phone">123.456.7890</div>
</section>

<section class="about">
  <div class="ring"></div>
  <div class="ph" role="img" aria-label="Smiling electrician in work gear with tool belt"></div>
  <div class="accent" role="img" aria-label="Orange lightning accent beside the portrait"></div>
  <div class="kicker">About</div>
  <h2>Voltline Systems</h2>
  <p>Lorem ipsum dolor sit amet, consectetuer adipiscing elit, sed diam nonummy nibh euismod tincidunt ut laoreet dolore magna aliquam erat volutpat. Ut wisi enim ad minim veniam, quis nostrud exerci tation ullamcorper suscipit lobortis nisl ut aliquip ex ea commodo consequat. Duis autem vel eum iriure dolor in hendrerit in vulputate velit esse molestie consequat, vel illum dolore eu feugiat nulla facilisis at vero eros et accumsan et iusto odio dignissim qui blandit praesent luptatum zzril delenit augue duis dolore te feugait nulla facilisi.</p>
  <div class="btn btn-navy">Read More</div>
</section>

<section class="services">
  <h2 class="sec-title"><span>Our</span> Services</h2>
  <div class="svc svc-business" role="img" aria-label="Office building in orange tint">
    <div class="frame"></div><div class="frame2"></div>
    <h3>Business</h3>
    <p>Lorem ipsum dolor sit amet, consectetuer adipiscing elit, sed diam nonummy nibh euismod tincidunt ut laoreet dolore magna aliquam erat volutpat. Ut wisi enim ad minim veniam, quis nostrud exerci tation ullamcorper suscipit lobortis nisl ut aliquip ex ea commodo consequat. Duis autem vel eum iriure dolor in hendrerit in vulputate velit esse molestie consequat.</p>
    <div class="btn btn-navy">Read More</div>
  </div>
  <div class="svc svc-home" role="img" aria-label="Family house in navy tint">
    <div class="frame"></div><div class="frame2"></div>
    <h3>Home Owner</h3>
    <p>Lorem ipsum dolor sit amet, consectetuer adipiscing elit, sed diam nonummy nibh euismod tincidunt ut laoreet dolore magna aliquam erat volutpat. Ut wisi enim ad minim veniam, quis nostrud exerci tation ullamcorper suscipit lobortis nisl ut aliquip ex ea commodo consequat. Duis autem vel eum iriure dolor in hendrerit in vulputate velit esse molestie consequat.</p>
    <div class="btn btn-orange">Read More</div>
  </div>
  <div class="notch"></div>
</section>

<section class="testimonials">
  <h2 class="sec-title"><span>Client</span> Testimonials</h2>
  <div class="quote-card side" style="left:180px">
    <span class="q" style="left:40px;top:24px">“</span>
    Lorem ipsum dolor sit amet, consectetuer adipiscing elit, sed diam nonummy nibh euismod tincidunt ut laoreet dolore magna aliquam erat volutpat. Ut wisi enim ad minim veniam, quis nostrud exerci tation ullamcorper
    <div class="stars"><svg width="90" height="14"><g fill="#f26a2e"><circle cx="7" cy="7" r="6"/><circle cx="26" cy="7" r="6"/><circle cx="45" cy="7" r="6"/><circle cx="64" cy="7" r="6"/><circle cx="83" cy="7" r="6"/></g></svg></div>
  </div>
  <div class="quote-card side" style="left:640px">
    <span class="q" style="right:40px;top:100px">”</span>
    Lorem ipsum dolor sit amet, consectetuer adipiscing elit, sed diam nonummy nibh euismod tincidunt ut laoreet dolore magna aliquam erat volutpat. Ut wisi enim ad minim veniam, quis nostrud exerci tation ullamcorper
    <div class="stars"><svg width="90" height="14"><g fill="#f26a2e"><circle cx="7" cy="7" r="6"/><circle cx="26" cy="7" r="6"/><circle cx="45" cy="7" r="6"/><circle cx="64" cy="7" r="6"/><circle cx="83" cy="7" r="6"/></g></svg></div>
  </div>
  <div class="quote-card center">
    <span class="q" style="left:16px;top:18px">“</span>
    <span class="q" style="right:16px;top:110px">”</span>
    Lorem ipsum dolor sit amet, consectetuer adipiscing elit, sed diam nonummy nibh euismod tincidunt ut laoreet dolore magna aliquam erat volutpat. Ut wisi enim ad minim veniam, quis nostrud exerci tation ullamcorper
    <div class="stars"><svg width="90" height="14"><g fill="#f26a2e"><circle cx="7" cy="7" r="6"/><circle cx="26" cy="7" r="6"/><circle cx="45" cy="7" r="6"/><circle cx="64" cy="7" r="6"/><circle cx="83" cy="7" r="6"/></g></svg></div>
  </div>
  <div class="avatar" role="img" aria-label="Client portrait"></div>
  <div class="client-name">Owen Tarrant</div>
</section>

<section class="emergency">
  <div class="ph" role="img" aria-label="Electrician sitting on a toolbox with hard hat"></div>
  <h2>24 Hours Emergency Service</h2>
  <p>Lorem ipsum dolor sit amet, consectetuer adipiscing elit, sed diam nonummy nibh euismod tincidunt ut laoreet dolore.</p>
  <div class="btn btn-orange">Contact Us Today</div>
</section>

<section class="team">
  <h2 class="sec-title"><span>Meet</span> the Team</h2>
  <div class="member" style="left:141px"><div class="ph" role="img" aria-label="Electrician in navy overalls and hard hat" style="background:linear-gradient(180deg,#ececec 0,#e6e6e6 30%,#3b4a72 55%,#2a3557)"></div></div>
  <div class="member" style="left:375px">
    <div class="ph" role="img" aria-label="Electrician with coiled cable" style="background:linear-gradient(180deg,#ececec 0,#d6b8a4 25%,#8a5a56 50%,#6d5b52)"></div>
    <div class="member-card"><h4>Dean Marlow</h4><div class="role">Electrician</div><div class="socials"><i></i><i></i><i></i><i></i></div></div>
  </div>
  <div class="member" style="left:612px"><div class="ph" role="img" aria-label="Electrician in blue apron with tool belt" style="background:linear-gradient(180deg,#ececec 0,#e9a46a 20%,#6f8fbf 50%,#2b4f9a)"></div></div>
  <div class="member" style="left:847px"><div class="ph" role="img" aria-label="Female electrician in navy polo with tool belt" style="background:linear-gradient(180deg,#ececec 0,#e7c985 22%,#27345a 55%,#2d3b61)"></div></div>
  <div class="btn btn-navy">View All</div>
</section>

<section class="projects">
  <h2 class="sec-title"><span>Our</span> Projects</h2>
  <div class="tile" role="img" aria-label="Testing a distribution board" style="left:141px;top:146px;width:220px;height:185px;background:linear-gradient(135deg,#7d8a96,#3e4a55)"></div>
  <div class="tile" role="img" aria-label="Electrician with hard hat at work" style="left:371px;top:146px;width:220px;height:240px;background:linear-gradient(135deg,#b5b0a7,#5d5e63)"></div>
  <div class="tile tile-hover" style="left:601px;top:146px;width:220px;height:175px"><div class="plus">+</div>Lorem ipsum dolor sit amet consectetuer</div>
  <div class="tile" role="img" aria-label="Electrician on a ladder fitting ceiling light" style="left:831px;top:146px;width:229px;height:225px;background:linear-gradient(135deg,#d9dbdf,#9aa3ae)"></div>
  <div class="tile" role="img" aria-label="Electrician wiring a panel" style="left:141px;top:341px;width:220px;height:222px;background:linear-gradient(135deg,#6f7f73,#c27a3e)"></div>
  <div class="tile" role="img" aria-label="Ceiling light installation" style="left:371px;top:396px;width:220px;height:167px;background:linear-gradient(135deg,#a9a8a2,#4f4d48)"></div>
  <div class="tile" role="img" aria-label="Close-up of hands cutting red wire" style="left:601px;top:331px;width:220px;height:232px;background:linear-gradient(135deg,#d8cfc6,#8d6f63)"></div>
  <div class="tile" role="img" aria-label="Workers installing wiring" style="left:831px;top:381px;width:229px;height:182px;background:linear-gradient(135deg,#aeb7c2,#4d5b6e)"></div>
  <div class="btn btn-navy">View All</div>
</section>

<footer class="site-footer">
  <div class="f-col" style="left:141px">
    <h5>Quick Links</h5>
    <ul class="f-links"><li>Home</li><li>Meet The Team</li><li>Services</li><li>Projects</li><li>Contact</li></ul>
  </div>
  <div class="f-col f-contact" style="left:328px">
    <h5>Contact Details</h5>
    <div class="row"><svg class="ic" width="12" height="14" viewBox="0 0 24 28"><path fill="#fff" d="M12 0a10 10 0 00-10 10c0 8 10 18 10 18s10-10 10-18A10 10 0 0012 0zm0 14a4 4 0 110-8 4 4 0 010 8z"/></svg><div><b>VOLTLINE SYSTEMS</b><br>123 Lorem ipsum dolor sit amet,<br>consectetuer adipiscing elit</div></div>
    <div class="row"><svg class="ic" width="12" height="12" viewBox="0 0 24 24"><path fill="#fff" d="M6.6 10.8a15 15 0 006.6 6.6l2.2-2.2c.3-.3.7-.4 1-.2 1.1.4 2.3.6 3.6.6.6 0 1 .4 1 1V20c0 .6-.4 1-1 1A17 17 0 013 4c0-.6.4-1 1-1h3.5c.6 0 1 .4 1 1 0 1.3.2 2.5.6 3.6.1.3 0 .7-.2 1z"/></svg>123-456-7890</div>
    <div class="row"><svg class="ic" width="12" height="12" viewBox="0 0 24 24"><path fill="#fff" d="M6 3h12v5H6zM3 9h18v9h-3v4H6v-4H3zm5 7v4h8v-4z"/></svg>123-456-7890</div>
    <div class="row"><svg class="ic" width="12" height="12" viewBox="0 0 24 24"><path fill="#fff" d="M2 5h20v14H2zm2 2v.5l8 5 8-5V7z"/></svg>info@voltlinesys.com</div>
  </div>
  <div class="f-col" style="left:612px">
    <h5>chirpnet Feeds</h5>
    <div class="feed"><span class="sq"></span><div class="t"><b>chirpnet@lorem ipsum</b>Lorem ipsum dolor sit consectetuer<br>adipiscing elit sed diam</div></div>
    <div class="feed"><span class="sq"></span><div class="t"><b>chirpnet@lorem ipsum</b>Lorem ipsum dolor sit consectetuer<br>adipiscing elit sed diam</div></div>
    <div class="feed"><span class="sq"></span><div class="t"><b>chirpnet@lorem ipsum</b>Lorem ipsum dolor sit consectetuer<br>adipiscing elit sed diam</div></div>
  </div>
  <div class="view-all">View All</div>
  <div class="f-brand">
    <div class="mark"></div>
    <div class="name">Voltline Systems</div>
    <div class="f-social"><i></i><i></i><i></i><i></i></div>
  </div>
</footer>
<div class="copyright">Copyright © 2019 VOLTLINE SYSTEMS. All Rights Reserved.</div>

</body>
</html>
```